Venture Keystone - Client Appreciation Party Invitation and Poster

We need a printable invitation, a version of the same invitation that can be emailed out, and also a Poster of the invitation for our annual client appreciation party.

The location is called: The Lanternhouse. Here is a link to the location: https://www.thelanternhousevenue.example/

We like their font and their little logo that you see when you log onto this page. But we'd love to see creatively what you can come up with.

This party is for our clients who are interior designers and owners in the Hospitality industry. Here are the details which need to be included in the invitation:

Location: The Lanternhouse - 482 W Brindle Ave. Chicago IL 60614
Date/Time: Thursday August 23rd - 5:30-9:00pm
RSVP: Please RSVP to: gathering@venturekeystone.example

Then our Sponsors Logos need to be included on the bottom: I have uploaded those logos here as well as our Logo and a copy of the invitation we did for last year's party so you can see sort of what we've done in the past.

For the poster - we typically do a version of the invitation (see uploaded example of last year's poster) with the sponsor logos and the overall theme of the invitation just a bit simplified by removing the date/time/location info. We need this in a printable format which can be blown up to a 24x30 poster size.

Requirements
Must have
• use 2 to 3 colors only.
• logos of sponsors can be of the same color.

```html
<!DOCTYPE html>
<html lang="en">
<head>
<meta charset="utf-8">
<title>Venture Keystone – Weekend Warm Up Client Appreciation Event</title>
<link rel="stylesheet" href="https://fonts.googleapis.com/css2?family=Great+Vibes&family=Mulish:wght@700;800&family=Playfair+Display:wght@700&display=swap">
<style>
  :root {
    --green: #1f4a36;
    --navy: #1d2f5a;
    --ink: #2b2a24;
    --parchment: #efe6cc;
    --paper: #f7f5ef;
  }
  * { margin: 0; padding: 0; box-sizing: border-box; }
  html, body { width: 776px; height: 1200px; overflow: hidden; background: var(--paper); }
  .invitation { position: relative; width: 776px; height: 1200px; overflow: hidden; }
  .backdrop { position: absolute; inset: 0; }
  .centered { position: absolute; left: 0; width: 100%; text-align: center; }

  .host {
    top: 34px; font-family: "Playfair Display", serif; font-weight: 700;
    font-size: 31px; letter-spacing: 1px; color: var(--green); text-transform: uppercase;
  }
  .event-name {
    font-family: "Great Vibes", cursive; color: var(--green);
    font-size: 104px; line-height: 1; text-shadow: 0 0 1px var(--green);
  }
  .event-name--first { top: 96px; }
  .event-name--second { top: 210px; }

  .headline {
    top: 522px; font-family: "Playfair Display", serif; font-weight: 700;
    font-size: 54px; line-height: 60px; color: var(--green); letter-spacing: 2px;
    text-transform: uppercase;
  }
  .venue { top: 722px; font-family: "Mulish", sans-serif; font-weight: 800; font-size: 30px; color: var(--navy); }
  .address { top: 774px; font-family: "Mulish", sans-serif; font-weight: 700; font-size: 25px; color: var(--ink); }
  .date { top: 820px; font-family: "Mulish", sans-serif; font-weight: 800; font-size: 24px; color: var(--navy); }
  .time { top: 854px; font-family: "Mulish", sans-serif; font-weight: 800; font-size: 26px; color: var(--green); }
  .sprig {
    position: absolute; left: 316px; top: 908px; width: 146px; height: 26px;
    border-radius: 13px; background: linear-gradient(90deg, rgba(31,74,54,0.12), rgba(31,74,54,0.35), rgba(31,74,54,0.12));
  }
  .rsvp { top: 974px; font-family: "Mulish", sans-serif; font-weight: 700; font-size: 20px; line-height: 30px; color: var(--ink); }

  .sponsors {
    position: absolute; left: 0; top: 1060px; width: 100%; height: 140px;
    display: flex; align-items: center; justify-content: space-around; padding: 0 24px;
  }
  .sponsor {
    display: flex; align-items: center; gap: 8px;
    font-family: "Mulish", sans-serif; font-weight: 800; font-size: 17px; color: var(--green);
  }
  .sponsor-mark { width: 14px; height: 14px; background: var(--green); }
</style>
</head>
<body>
<main class="invitation">
  <svg class="backdrop" width="776" height="1200" viewBox="0 0 776 1200">
    <defs>
      <linearGradient id="venue-photo-tone" x1="0" y1="0" x2="1" y2="1">
        <stop offset="0" stop-color="#c9b6a2"/>
        <stop offset="0.45" stop-color="#e6e1da"/>
        <stop offset="0.75" stop-color="#9fb3c4"/>
        <stop offset="1" stop-color="#7d8f9a"/>
      </linearGradient>
      <linearGradient id="parchment-tone" x1="0" y1="0" x2="0" y2="1">
        <stop offset="0" stop-color="#efe7cf"/>
        <stop offset="1" stop-color="#ebe2c6"/>
      </linearGradient>
    </defs>
    <rect x="0" y="0" width="776" height="560" fill="url(#venue-photo-tone)" role="img"
      aria-label="Photo of a long banquet table set with white plates, blue velvet chairs and potted green plants in a bright loft dining room"/>
    <path class="panel" d="M0 545 Q388 421 776 545 L776 1052 L0 1052 Z" fill="url(#parchment-tone)" role="img"
      aria-label="Parchment panel with faint watercolour leaf branches"/>
    <path class="panel-edge" d="M0 545 Q388 421 776 545" fill="none" stroke="var(--green)" stroke-width="5"/>
    <rect class="footer-rule" x="0" y="1050" width="776" height="8" fill="var(--green)"/>
    <rect class="footer" x="0" y="1058" width="776" height="142" fill="var(--paper)"/>
  </svg>

  <p class="centered host">Venture Keystone</p>
  <h1>
    <span class="centered event-name event-name--first">Weekend</span>
    <span class="centered event-name event-name--second">Warm Up</span>
  </h1>

  <h2 class="centered headline">Client<br>Appreciation<br>Event</h2>
  <p class="centered venue">The Lanternhouse</p>
  <p class="centered address">482 W Brindle Ave. Chicago IL 60614</p>
  <p class="centered date">Thursday August 23rd, 2018</p>
  <p class="centered time">5:30-9:00pm</p>
  <div class="sprig" role="img" aria-label="Small watercolour leaf sprig ornament"></div>
  <p class="centered rsvp">Please RSVP to:<br>gathering@venturekeystone.example</p>

  <footer class="sponsors">
    <span class="sponsor"><span class="sponsor-mark"></span>Dovetail</span>
    <span class="sponsor">Kestrel Hospitality</span>
    <span class="sponsor">Brightwell Lighting</span>
    <span class="sponsor">Solenne</span>
    <span class="sponsor"><span class="sponsor-mark"></span>Arbor Trade</span>
  </footer>
</main>
</body>
</html>
```